flat share room mate rental website(design only)

We need a design for the homepage of a flat share / roommate website. We have a website template http://demo1.hometemplix.net and we're looking for a homepage similar to this http://uk.bunkpalora.com but different.
The main user of the site are likely to be students and young professionals so were not looking for anything too serious.
We want to emphasise that the website will be 100% free to use both to post an advert and to contact the advertiser.
We must have a 'new rooms' and new flatmates carousel, also we would prefer if the menu had only a login button and maybe a 'post a room' button.
Our logo is currently being designed, so you can put anything in its place.
We look forward to seeing what you guys come up with.
Target Market(s)
Students, Young Professionals
Industry/Entity Type
Rental
Number of Pages Required
1 page
Look and feel
Each slider illustrates characteristics of the customer's brand and the style your logo design should communicate.

```html
<!DOCTYPE html>
<html lang="en">
<head>
<meta charset="utf-8">
<title>Flatshare Homepage</title>
<link href="https://fonts.googleapis.com/css2?family=Oswald:wght@400;500&family=Open+Sans:wght@400;600;700&display=swap" rel="stylesheet">
<style>
:root{
  --orange:#f7a13d;
  --pink:#f28b8f;
  --blue:#72c4e4;
  --teal:#6dcfbe;
  --ink:#2b2b2b;
  --text:#6a6a6a;
  --muted:#9a9a9a;
  --light:#e9e9e9;
  --card:#ececec;
  --card-bar:#c9c9c9;
  --footer:#262626;
  --footer-bottom:#1c1c1c;
  --white:#ffffff;
}
*{box-sizing:border-box;margin:0;padding:0}
html,body{width:1200px;height:2981px;overflow:hidden}
body{position:relative;background:var(--white);font-family:"Open Sans",Arial,sans-serif;color:var(--text)}
.section{position:absolute;left:0;width:1200px}
.heading{font-family:"Oswald",Arial,sans-serif;font-weight:400;text-transform:uppercase;color:var(--ink)}

/* header */
.site-header{top:0;height:65px;background:var(--white)}
.logo{position:absolute;left:75px;top:18px;font-family:"Oswald",sans-serif;font-size:24px;font-weight:500;color:var(--ink)}
.logo span{color:var(--orange)}
.nav{position:absolute;right:84px;top:24px;display:flex;gap:30px;font-size:13px;font-weight:700;text-transform:uppercase}
.nav .login{color:var(--ink)}
.nav .post{color:var(--orange);font-weight:600}

/* hero */
.hero{top:65px;height:576px;background:linear-gradient(180deg,#3a2c25 0%,#5a4336 45%,#2e221c 100%)}
.hero-title{position:absolute;top:290px;width:100%;text-align:center;font-family:"Oswald",sans-serif;font-size:50px;font-weight:400;color:var(--white);text-transform:uppercase}
.search-box{position:absolute;left:206px;top:390px;width:788px;height:86px;background:rgba(255,255,255,.28)}
.select{position:absolute;left:23px;top:24px;width:392px;height:38px;background:var(--white);border:1px solid #ccc;font-size:12px;color:#666;padding:10px 12px}
.select svg{position:absolute;right:12px;top:14px}
.btn{position:absolute;height:38px;line-height:38px;text-align:center;color:var(--white);font-size:13px;font-weight:600;text-transform:uppercase}
.btn-orange{background:var(--orange)}
.btn-pink{background:var(--pink)}
.hero-note{position:absolute;top:492px;width:100%;text-align:center;font-family:"Oswald",sans-serif;font-size:19px;line-height:25px;color:var(--white);text-transform:uppercase}
.hero-note b{color:var(--orange);font-weight:400}

/* stats */
.stats{top:641px;height:303px;background:var(--light)}
.stats-title{position:absolute;top:45px;width:100%;text-align:center;font-size:24px}
.feature{position:absolute;top:112px;width:330px}
.feature .icon{position:absolute;left:0;top:0;width:58px;height:58px;border-radius:50%;display:flex;align-items:center;justify-content:center}
.feature h3{position:absolute;left:80px;top:16px;font-size:17px;font-family:"Oswald",sans-serif;font-weight:400;color:var(--ink);text-transform:uppercase}
.feature p{position:absolute;left:80px;top:58px;width:250px;font-size:13px;line-height:21px}

/* generic block heading + arrows */
.block-title{position:absolute;left:75px;font-size:24px}
.arrows{position:absolute;left:1073px;display:flex;gap:6px}
.arrows span{width:24px;height:24px;display:flex;align-items:center;justify-content:center}
.arrows .prev{background:#c8c8c8}
.arrows .next{background:var(--orange)}

/* rooms */
.rooms{top:944px;height:410px}
.room{position:absolute;top:99px;width:242px;height:254px;background:var(--card)}
.room .photo{position:absolute;left:12px;top:17px;width:218px;height:122px;background:linear-gradient(135deg,#8a6a52,#d8cbbd 55%,#6a5444)}
.room p{position:absolute;left:12px;top:155px;width:218px;font-size:12px;line-height:19px}
.room .bar{position:absolute;left:0;bottom:0;width:100%;height:28px;background:var(--card-bar);color:var(--white);font-size:12px;display:flex;align-items:center;justify-content:space-between;padding:0 12px}
.room .bar .loc{display:flex;align-items:center;gap:6px}
.room .bar .price{font-weight:600}

/* banners */
.banner{background:linear-gradient(120deg,#5a2b26,#b98a72 50%,#4a3b35)}
.banner-text{position:absolute;width:100%;text-align:center;font-family:"Oswald",sans-serif;color:var(--white);text-transform:uppercase}
.home-banner{top:1354px;height:228px}
.home-banner .banner-text{top:60px;font-size:42px;line-height:49px}

/* flatmates */
.flatmates{top:1582px;height:378px}
.mate{position:absolute;top:107px;width:243px}
.mate .photo{height:137px;background:linear-gradient(135deg,#cfc6bd,#8c7a6e)}
.mate .name{margin-top:17px;display:flex;align-items:center;gap:8px;font-size:13px;font-weight:700;color:var(--ink)}
.mate p{margin-top:8px;font-size:12px;line-height:19px}

.cta{top:1960px;height:191px}
.cta .banner-text{top:40px;font-size:32px}

/* community */
.community{top:2151px;height:398px}
.member{position:absolute;top:104px;width:243px}
.member .photo{height:140px;background:linear-gradient(135deg,#d9d4cc,#7d6d60)}
.member .name{margin-top:16px;font-size:12px;font-weight:700;color:var(--ink);text-transform:uppercase}
.member .date{font-size:11px;color:var(--muted);margin-top:2px}
.member p{margin-top:9px;font-size:12px;line-height:19px}

/* footer */
.site-footer{top:2549px;height:432px;background:var(--footer)}
.foot-col{position:absolute;top:50px;width:230px}
.foot-col h4{font-size:12px;font-weight:700;color:var(--white);text-transform:uppercase;margin-bottom:10px}
.foot-col li{list-style:none;font-size:12px;line-height:20.6px;color:#a8a8a8}
.foot-col li.all{color:var(--white);margin-top:8px}
.social{display:flex;gap:6px;margin-top:10px}
.social span{width:24px;height:24px;border:1.5px solid #8a8a8a;border-radius:50%}
.foot-bottom{position:absolute;left:0;bottom:0;width:1200px;height:60px;background:var(--footer-bottom);font-size:12px;color:#a8a8a8}
.foot-bottom .copy{position:absolute;left:75px;top:22px}
.foot-bottom .legal{position:absolute;right:75px;top:22px;display:flex;gap:16px}
</style>
</head>
<body>

<header class="section site-header">
  <div class="logo">LOGO <span>HERE</span></div>
  <nav class="nav"><span class="login">Login</span><span class="post">Post a room</span></nav>
</header>

<section class="section hero" role="img" aria-label="Photo of a bright bedroom with large windows">
  <h1 class="hero-title">Find your perfect flatmate</h1>
  <div class="search-box">
    <div class="select">Select a location
      <svg width="10" height="6" viewBox="0 0 10 6"><path d="M1 1l4 4 4-4" stroke="#555" stroke-width="1.5" fill="none"/></svg>
    </div>
    <div class="btn btn-orange" style="left:430px;top:24px;width:161px">I need a room</div>
    <div class="btn btn-pink" style="left:601px;top:24px;width:164px">I have a room</div>
  </div>
  <p class="hero-note"><b>No fees.</b> We don't charge you anything.<br>That means no fees to post an advert and no fees to contact your potential new flatmate.</p>
</section>

<section class="section stats">
  <h2 class="heading stats-title">5,456,267 happy flatshares and counting...</h2>
  <div class="feature" style="left:75px">
    <div class="icon" style="background:var(--orange)"><svg width="26" height="26" viewBox="0 0 24 24"><path d="M12 2a7 7 0 0 0-7 7c0 5 7 13 7 13s7-8 7-13a7 7 0 0 0-7-7z" fill="none" stroke="#fff" stroke-width="2"/><circle cx="12" cy="9" r="2.5" fill="#fff"/></svg></div>
    <h3>Great rooms</h3>
    <p>In publishing and graphic design, lorem ipsum is a filler text commonly used to demonstrate the graphic elements of a document or visual presentation.</p>
  </div>
  <div class="feature" style="left:435px">
    <div class="icon" style="background:var(--blue)"><svg width="26" height="26" viewBox="0 0 24 24"><circle cx="10" cy="10" r="6" fill="none" stroke="#fff" stroke-width="2"/><path d="M15 15l6 6" stroke="#fff" stroke-width="2.5"/></svg></div>
    <h3>Easy search</h3>
    <p>In publishing and graphic design, lorem ipsum is a filler text commonly used to demonstrate the graphic elements of a document or visual presentation.</p>
  </div>
  <div class="feature" style="left:795px">
    <div class="icon" style="background:var(--teal)"><svg width="26" height="26" viewBox="0 0 24 24"><path d="M3 5h18v11H9l-5 4v-4H3z" fill="none" stroke="#fff" stroke-width="2"/><circle cx="8" cy="10.5" r="1.2" fill="#fff"/><circle cx="12" cy="10.5" r="1.2" fill="#fff"/><circle cx="16" cy="10.5" r="1.2" fill="#fff"/></svg></div>
    <h3>Expert help 24/7</h3>
    <p>In publishing and graphic design, lorem ipsum is a filler text commonly used to demonstrate the graphic elements of a document or visual presentation.</p>
  </div>
</section>

<section class="section rooms">
  <h2 class="heading block-title" style="top:50px">New rooms to rent</h2>
  <div class="arrows" style="top:56px">
    <span class="prev"><svg width="8" height="10" viewBox="0 0 8 10"><path d="M6 1L2 5l4 4" stroke="#fff" stroke-width="2" fill="none"/></svg></span>
    <span class="next"><svg width="8" height="10" viewBox="0 0 8 10"><path d="M2 1l4 4-4 4" stroke="#fff" stroke-width="2" fill="none"/></svg></span>
  </div>
  <div class="room" style="left:75px">
    <div class="photo" role="img" aria-label="Photo of a double bedroom"></div>
    <p>In publishing and graphic design, lorem document or visual design presentation.</p>
    <div class="bar"><span class="loc"><svg width="9" height="12" viewBox="0 0 9 12"><path d="M4.5 0A4.5 4.5 0 0 0 0 4.5C0 8 4.5 12 4.5 12S9 8 9 4.5A4.5 4.5 0 0 0 4.5 0z" fill="#fff"/></svg>Wolverhampton</span><span class="price">$250 pcm</span></div>
  </div>
  <div class="room" style="left:345px">
    <div class="photo" role="img" aria-label="Photo of a bedroom with curtains" style="background:linear-gradient(135deg,#5a3a22,#c79a55 50%,#3b2a1e)"></div>
    <p>In publishing and graphic design, lorem document or visual design presentation.</p>
    <div class="bar"><span class="loc"><svg width="9" height="12" viewBox="0 0 9 12"><path d="M4.5 0A4.5 4.5 0 0 0 0 4.5C0 8 4.5 12 4.5 12S9 8 9 4.5A4.5 4.5 0 0 0 4.5 0z" fill="#fff"/></svg>Wolverhampton</span><span class="price">$250 pcm</span></div>
  </div>
  <div class="room" style="left:616px">
    <div class="photo" role="img" aria-label="Photo of a bed with white linen" style="background:linear-gradient(135deg,#3a3330,#bdb6ae 55%,#5a4f48)"></div>
    <p>In publishing and graphic design, lorem document or visual design presentation.</p>
    <div class="bar"><span class="loc"><svg width="9" height="12" viewBox="0 0 9 12"><path d="M4.5 0A4.5 4.5 0 0 0 0 4.5C0 8 4.5 12 4.5 12S9 8 9 4.5A4.5 4.5 0 0 0 4.5 0z" fill="#fff"/></svg>Wolverhampton</span><span class="price">$250 pcm</span></div>
  </div>
  <div class="room" style="left:884px">
    <div class="photo" role="img" aria-label="Photo of a light bedroom" style="background:linear-gradient(135deg,#c9c2b4,#eeeae2 55%,#9a8b74)"></div>
    <p>In publishing and graphic design, lorem document or visual design presentation.</p>
    <div class="bar"><span class="loc"><svg width="9" height="12" viewBox="0 0 9 12"><path d="M4.5 0A4.5 4.5 0 0 0 0 4.5C0 8 4.5 12 4.5 12S9 8 9 4.5A4.5 4.5 0 0 0 4.5 0z" fill="#fff"/></svg>Wolverhampton</span><span class="price">$250 pcm</span></div>
  </div>
</section>

<section class="section banner home-banner" role="img" aria-label="Photo of friends holding hands">
  <p class="banner-text">Helping you find a flatshare<br>you can call home</p>
</section>

<section class="section flatmates">
  <h2 class="heading block-title" style="top:52px">New flatmates</h2>
  <div class="arrows" style="top:58px">
    <span class="prev"><svg width="8" height="10" viewBox="0 0 8 10"><path d="M6 1L2 5l4 4" stroke="#fff" stroke-width="2" fill="none"/></svg></span>
    <span class="next"><svg width="8" height="10" viewBox="0 0 8 10"><path d="M2 1l4 4-4 4" stroke="#fff" stroke-width="2" fill="none"/></svg></span>
  </div>
  <div class="mate" style="left:75px"><div class="photo" role="img" aria-label="Portrait photo of a new flatmate"></div><div class="name"><svg width="12" height="12" viewBox="0 0 12 12"><circle cx="6" cy="3.5" r="3" fill="#2b2b2b"/><path d="M0 12c0-4 3-5.5 6-5.5s6 1.5 6 5.5z" fill="#2b2b2b"/></svg>Lorem Ipsu 31</div><p>In publishing and graphic design, lorem document or visual presentation.</p></div>
  <div class="mate" style="left:345px"><div class="photo" role="img" aria-label="Portrait photo of a new flatmate" style="background:linear-gradient(135deg,#e4ddd3,#7a6352)"></div><div class="name"><svg width="12" height="12" viewBox="0 0 12 12"><circle cx="6" cy="3.5" r="3" fill="#2b2b2b"/><path d="M0 12c0-4 3-5.5 6-5.5s6 1.5 6 5.5z" fill="#2b2b2b"/></svg>Lorem Ipsu 31</div><p>In publishing and graphic design, lorem document or visual presentation.</p></div>
  <div class="mate" style="left:614px"><div class="photo" role="img" aria-label="Photo of two new flatmates outdoors" style="background:linear-gradient(135deg,#8fa0a8,#5a4a58)"></div><div class="name"><svg width="12" height="12" viewBox="0 0 12 12"><circle cx="6" cy="3.5" r="3" fill="#2b2b2b"/><path d="M0 12c0-4 3-5.5 6-5.5s6 1.5 6 5.5z" fill="#2b2b2b"/></svg>Lorem Ipsu 31</div><p>In publishing and graphic design, lorem document or visual presentation.</p></div>
  <div class="mate" style="left:882px"><div class="photo" role="img" aria-label="Portrait photo of a new flatmate" style="background:linear-gradient(135deg,#d8d4cc,#5c4a40)"></div><div class="name"><svg width="12" height="12" viewBox="0 0 12 12"><circle cx="6" cy="3.5" r="3" fill="#2b2b2b"/><path d="M0 12c0-4 3-5.5 6-5.5s6 1.5 6 5.5z" fill="#2b2b2b"/></svg>Lorem Ipsu 31</div><p>In publishing and graphic design, lorem document or visual presentation.</p></div>
</section>

<section class="section banner cta" role="img" aria-label="Photo of a group of young people" style="background:linear-gradient(120deg,#3a2a24,#7a5a48 50%,#2e241f)">
  <p class="banner-text">Find your perfect flatshare today!</p>
  <div class="btn btn-orange" style="left:395px;top:99px;width:199px">Start your search</div>
  <div class="btn btn-pink" style="left:611px;top:99px;width:191px">Post your room</div>
</section>

<section class="section community">
  <h2 class="heading block-title" style="top:50px">Our community</h2>
  <div class="arrows" style="top:56px">
    <span class="prev"><svg width="8" height="10" viewBox="0 0 8 10"><path d="M6 1L2 5l4 4" stroke="#fff" stroke-width="2" fill="none"/></svg></span>
    <span class="next"><svg width="8" height="10" viewBox="0 0 8 10"><path d="M2 1l4 4-4 4" stroke="#fff" stroke-width="2" fill="none"/></svg></span>
  </div>
  <div class="member" style="left:75px"><div class="photo" role="img" aria-label="Portrait photo of a community member"></div><div class="name">John</div><div class="date">12-Sep-2014</div><p>In publishing and graphic design, lorem document or visual presentation.</p></div>
  <div class="member" style="left:345px"><div class="photo" role="img" aria-label="Portrait photo of a community member" style="background:linear-gradient(135deg,#d4dccf,#3a6a6a)"></div><div class="name">John</div><div class="date">12-Sep-2014</div><p>In publishing and graphic design, lorem document or visual presentation.</p></div>
  <div class="member" style="left:614px"><div class="photo" role="img" aria-label="Portrait photo of a community member" style="background:linear-gradient(135deg,#c8a878,#6a5038)"></div><div class="name">John</div><div class="date">12-Sep-2014</div><p>In publishing and graphic design, lorem document or visual presentation.</p></div>
  <div class="member" style="left:882px"><div class="photo" role="img" aria-label="Portrait photo of a community member" style="background:linear-gradient(135deg,#e0ddd8,#5a5048)"></div><div class="name">John</div><div class="date">12-Sep-2014</div><p>In publishing and graphic design, lorem document or visual presentation.</p></div>
</section>

<footer class="section site-footer">
  <div class="foot-col" style="left:75px">
    <h4>Popular cities</h4>
    <ul>
      <li>Birmingham flatshare</li><li>Bristol flatshare</li><li>Coventry flatshare</li><li>Leeds flatshare</li><li>Liverpool flatshare</li><li>London flatshare</li><li>Manchester flatshare</li><li>Newcastle upon Tyne flatshare</li><li>Nottingham flatshare</li><li>Sheffield flatshare</li><li class="all">All cities</li>
    </ul>
  </div>
  <div class="foot-col" style="left:345px">
    <h4>Flatshare types</h4>
    <ul>
      <li>Bedsits And Studios</li><li>Double Room Flatshare</li><li>DSS</li><li>Female Flatshare</li><li>Monday to Friday</li><li>Professional Flatshare</li><li>Roomshare</li><li>Short Let</li><li>Single Room Flatshare</li><li>Spare Room And Lodger</li><li>Student Accommodation</li>
    </ul>
  </div>
  <div class="foot-col" style="left:614px">
    <h4>About us</h4>
    <ul>
      <li>Need help?</li><li>FAQs</li><li>Press Room</li><li>Website Visitor &amp; User Agreements</li><li>Right-To-Rent</li><li>Become an Affiliate</li><li>Our Pledge</li>
    </ul>
  </div>
  <div class="foot-col" style="left:884px">
    <h4>Discover</h4>
    <ul><li>Landlord Zone</li><li>Our Blog</li></ul>
    <h4 style="margin-top:40px">Stay connected</h4>
    <div class="social"><span></span><span></span><span></span><span></span><span></span></div>
  </div>
  <div class="foot-bottom">
    <span class="copy">©2015 - Company Name here. All Rights Reserved.</span>
    <span class="legal"><span>Privacy Policy</span><span>Terms of Use</span></span>
  </div>
</footer>

</body>
</html>
```